Dental website design - brightmolarstudio.com

We are looking to do a redesign for the website: brightmolarstudio.com

Please use Sections from this google Slide I created: https://files.vextorashare.com/deck/8qLm3ZtR7wPaN2cYdK5uFh9JsB4eGx0VnTiQ6oMrXy1/view#page=p

Target Market(s)

Dentistry

Industry/Entity Type

Dental Clinic

Number of Pages Required

1 page

Colors
f68e4e
86cae7

Requirements
Must have
• Please use Sections from this google Slide I created: https://files.vextorashare.com/deck/8qLm3ZtR7wPaN2cYdK5uFh9JsB4eGx0VnTiQ6oMrXy1/view#page=p

```html
<!DOCTYPE html>
<html lang="en">
<head>
<meta charset="utf-8">
<title>Bright Molar Studio – Cosmetic Dentistry</title>
<link href="https://fonts.googleapis.com/css2?family=Playfair+Display:ital,wght@0,700;0,900;1,400;1,600&family=Montserrat:wght@400;500;600;700&display=swap" rel="stylesheet">
<style>
:root{
  --purple:#534a80;
  --purple-dark:#3f3670;
  --heading:#3d3371;
  --orange:#d2680a;
  --gold:#e0a848;
  --ink:#3b3b4a;
  --muted:#7b7b8c;
  --soft:#f6f6fb;
  --line:#b9b4d2;
  --white:#ffffff;
  --serif:'Playfair Display', Georgia, serif;
  --sans:'Montserrat', Arial, sans-serif;
}
*{box-sizing:border-box;margin:0;padding:0}
html,body{width:1200px;height:4713px;overflow:hidden}
body{font-family:var(--sans);color:var(--ink);background:var(--soft);position:relative}
section,header,footer{position:relative;width:1200px;overflow:hidden}
.abs{position:absolute}
.wave{display:block}
.title{font-family:var(--serif);font-weight:900;color:var(--heading);letter-spacing:.2px}
.center{left:0;right:0;text-align:center}
.btn{position:absolute;background:var(--orange);color:var(--white);font-family:var(--sans);font-weight:700;text-transform:uppercase;display:flex;align-items:center;justify-content:center;text-decoration:none}

/* header */
.site-header{height:113px;background:var(--white)}
.topbar{position:absolute;top:0;left:366px;right:0;height:33px;background:var(--purple);clip-path:polygon(36px 0,100% 0,100% 100%,0 100%)}
.topbar-item{position:absolute;top:0;height:33px;display:flex;align-items:center;gap:10px;color:var(--white);font-size:10px}
.brand{position:absolute;left:80px;top:34px;display:flex;align-items:center;gap:10px}
.brand-dot{width:22px;height:22px;border-radius:50%;background:var(--orange)}
.brand-name{font-family:var(--sans);font-weight:700;font-size:13px;color:var(--orange);text-transform:uppercase;line-height:1.2;width:150px}
.nav{position:absolute;left:0;top:33px;height:79px;width:1200px}
.nav a{position:absolute;top:0;height:79px;display:flex;align-items:center;font-size:10.5px;font-weight:600;color:var(--ink);text-decoration:none;text-transform:uppercase;white-space:nowrap}
.nav a::after{content:" ▾";font-size:8px;margin-left:3px}
.nav a.contact{background:var(--orange);color:var(--white);width:90px;justify-content:center}

/* hero */
.hero{height:487px;background:linear-gradient(100deg,#e9e8ee 0%,#d9d5e3 35%,#cbbfdc 55%,#d7cfd3 75%,#e4e1e6 100%)}
.hero h1{position:absolute;left:86px;top:192px;font-family:var(--serif);font-weight:900;font-size:45px;line-height:54px;color:var(--heading)}
.hero p{position:absolute;left:86px;top:344px;font-size:13.5px;line-height:17px;color:#222;width:330px}
.hero .btn{left:86px;top:421px;width:128px;height:44px;font-size:11px}

/* about */
.about{height:600px;background:var(--purple)}
.about h2{position:absolute;top:655px;font-size:20px;color:var(--white)}
.about-copy{position:absolute;left:243px;width:714px;top:150px;color:#e8e6f2;font-size:13.5px;line-height:26px;text-align:center}
.about-copy p+p{margin-top:24px}
.learn{position:absolute;top:380px;font-family:var(--serif);font-weight:700;font-size:14px;color:var(--gold);text-decoration:underline}

/* mission */
.mission{height:720px;background:var(--soft)}
.mission h2{position:absolute;left:146px;top:55px;font-size:18px}
.mission-copy{position:absolute;left:145px;top:150px;width:300px;font-size:11.5px;line-height:21px;color:var(--ink)}
.mission-copy p+p{margin-top:21px}
.social{position:absolute;left:146px;top:552px;display:flex;gap:52px}
.social span{width:18px;height:18px;border-radius:50%;background:var(--heading)}
.mission .btn{left:144px;top:611px;width:154px;height:48px;font-size:11px;text-transform:none}
.mission small{position:absolute;left:144px;top:668px;font-size:9.5px;color:var(--muted)}

/* testimonials */
.testimonials{height:598px;background:var(--soft)}
.testimonials h2{position:absolute;top:60px;font-size:28px}
.quote{position:absolute;left:240px;width:720px;top:192px;text-align:center;font-family:var(--serif);font-style:italic;font-size:10.6px;line-height:34px;color:#222}
.quote a{color:var(--heading);font-weight:600;text-decoration:none}
.avatar{position:absolute;border-radius:50%;border:3px solid #cfcbe0}
.dots{position:absolute;top:540px;left:571px;display:flex;gap:12px}
.dots span{width:8px;height:8px;border-radius:50%;background:#8e8aa6}
.dots span.on{background:var(--white);border:2px solid #4d68b8;width:10px;height:10px;margin-top:-1px}

/* why */
.why{height:789px;background:var(--purple)}
.why h2{position:absolute;top:68px;font-size:28px;color:var(--white)}
.feature{position:absolute;width:300px;text-align:center;color:var(--white)}
.feature svg{display:block;margin:0 auto}
.feature h3{font-family:var(--sans);font-weight:500;font-size:13px;text-transform:uppercase;margin-top:16px;letter-spacing:.3px}
.feature p{font-size:11.5px;line-height:17px;color:#cfcbe3;margin:14px auto 0;width:200px}

/* schedule */
.schedule{height:565px;background:var(--soft)}
.schedule h2{position:absolute;top:60px;font-size:27px}
.schedule-copy{position:absolute;left:243px;width:714px;top:176px;text-align:center;font-style:italic;font-size:10.5px;line-height:20.5px;color:var(--muted)}
.schedule-copy p+p{margin-top:20px}
.schedule .btn{left:472px;top:417px;width:256px;height:38px;font-size:11px}

/* contact */
.contact{height:454px;background:var(--purple)}
.map{position:absolute;left:0;top:0;width:618px;height:454px;background:linear-gradient(135deg,#eef0ee 0%,#e4e6e2 45%,#d7e3ea 70%,#e9ebe6 100%)}
.contact h2{position:absolute;left:695px;top:62px;font-size:26px;color:var(--white)}
.field{position:absolute;left:691px;width:249px;background:#6b62a0;border:1px solid #857dbb;color:#d8d4ec;font-size:9px;padding:9px 16px}
.submit{position:absolute;left:691px;top:362px;width:249px;height:39px;background:var(--white);color:var(--heading);font-size:10.5px;font-weight:700;display:flex;align-items:center;justify-content:center;text-transform:uppercase}

/* footer */
.site-footer{height:387px;background:var(--soft)}
.fcol{position:absolute;top:68px}
.fcol h4{font-family:var(--serif);font-weight:900;font-size:14px;color:var(--heading)}
.fcol ul{list-style:none;margin-top:30px}
.fcol li{font-size:10px;line-height:25.6px;color:var(--ink)}
.article{display:flex;gap:14px;height:77px}
.thumb{width:52px;height:50px;background:linear-gradient(135deg,#1e3f8a,#7fb4e6)}
.article p{font-size:10px;line-height:17px;color:var(--ink);width:230px}
.article time{display:block;color:#b5b4c2;font-size:10px}
.connect{display:flex;gap:14px;align-items:flex-start;font-size:10px;line-height:15px;margin-bottom:20px}
.rule{position:absolute;left:0;right:0;top:365px;height:1px;background:var(--line)}
</style>
</head>
<body>
<svg width="0" height="0" style="position:absolute">
  <defs>
    <pattern id="wave-light" width="6" height="6" patternUnits="userSpaceOnUse"><path d="M0 3 Q1.5 0 3 3 T6 3" fill="none" stroke="#d9d5ee" stroke-width="1"/></pattern>
    <pattern id="wave-dark" width="6" height="6" patternUnits="userSpaceOnUse"><path d="M0 3 Q1.5 0 3 3 T6 3" fill="none" stroke="#4d4585" stroke-width="1"/></pattern>
  </defs>
</svg>

<header class="site-header">
  <div class="topbar"></div>
  <div class="topbar-item" style="left:732px">
    <svg width="14" height="14" viewBox="0 0 14 14"><circle cx="7" cy="7" r="6.3" fill="none" stroke="#fff"/><path d="M4 7.5 10 4 7.5 10 6.6 7.6Z" fill="#fff"/></svg>
    418 Alder Ln #120 Fairview, OH 43999
  </div>
  <div class="topbar-item" style="left:1015px">
    <svg width="14" height="14" viewBox="0 0 14 14"><circle cx="7" cy="7" r="6.3" fill="none" stroke="#fff"/><path d="M5 4c-.8.4-1 1.3-.5 2.4.7 1.6 1.8 2.8 3.3 3.4 1 .4 1.8.2 2.2-.5L8.8 8.2l-.9.6C7 8.4 6.2 7.6 5.8 6.7l.6-.9Z" fill="#fff"/></svg>
    555 014 2287
  </div>
  <div class="brand"><span class="brand-dot"></span><span class="brand-name">Bright Molar Studio</span></div>
  <nav class="nav">
    <a style="left:267px">Preventative Care</a>
    <a style="left:423px">Get In Touch</a>
    <a style="left:538px">Patient Information</a>
    <a style="left:708px">Dental Implants</a>
    <a style="left:851px">Restorative Dentistry</a>
    <a class="contact" style="left:1019px">Contact</a>
  </nav>
</header>

<section class="hero" role="img" aria-label="Photo of a smiling woman pointing at her teeth on a soft lavender background">
  <h1>Cosmetic Dentistry for a<br>Dazzling New Smile</h1>
  <p>Efficient growth hack methods to build and promote products and companies</p>
  <a class="btn">Get In Touch</a>
</section>

<section class="about">
  <div class="abs" role="img" aria-label="Photo of dental mirror and probe instruments" style="left:0;top:296px;width:400px;height:304px;background:radial-gradient(ellipse at 55% 55%,rgba(220,220,230,.35),rgba(83,74,128,0) 65%)"></div>
  <div class="abs" role="img" aria-label="Illustration of two cheerful cartoon teeth" style="left:878px;top:378px;width:183px;height:183px;background:radial-gradient(circle,rgba(255,255,255,.55),rgba(83,74,128,0) 68%)"></div>
  <h2 class="title center" style="top:55px">About Growth Hack</h2>
  <svg class="wave abs" style="left:497px;top:92px" width="206" height="6"><rect width="206" height="6" fill="url(#wave-light)"/></svg>
  <div class="about-copy">
    <p>Lorem ipsum dolor sit amet, consectetur adipiscing elit, sed do eiusmod tempor incididunt ut labore et dolore magna aliqua. Ut enim ad minim veniam, quis nostrud exercitation ullamco laboris nisi ut.</p>
    <p>Duis aute irure dolor in reprehenderit in voluptate velit esse cillum dolore eu fugiat nulla pariatur. Excepteur sint occaecat cupidatat non proident, sunt in culpa qui officia deserunt mollit anim id est laborum. Sed ut perspiciatis unde omnis iste natus error sit voluptatem accusantium doloremque laudantium, totam rem aperiam, eaque ipsa quae ab illo inventore veritatis et quasi</p>
  </div>
  <a class="learn center">Learn more</a>
</section>

<section class="mission">
  <h2 class="title">Our Mission</h2>
  <svg class="wave abs" style="left:146px;top:90px" width="120" height="6"><rect width="120" height="6" fill="url(#wave-dark)"/></svg>
  <div class="mission-copy">
    <p>To be Committed to Dental Excellence in all our services that we provide to our patients.</p>
    <p>To constantly strive to achieve the highest level of skills and modern techniques and equipment so we can provide our patients with the best that Dentistry has to offer.</p>
    <p>Our vision is to be able to serve our patients and provide them with Modern Dentistry in a Comfortable Relaxed Environment.</p>
    <p>We provide our patients with a Caring dental experience that helps them build a long-term relationship that is built on knowledge of their dental needs, trust, confidence, quality of work, and exceptional patient care.</p>
  </div>
  <div class="social"><span></span><span></span><span></span><span></span></div>
  <a class="btn">Book an appointment</a>
  <small>Learn more about appointment</small>
  <div class="abs" role="img" aria-label="Photo of a smiling patient in a dental chair with a dentist holding instruments" style="left:574px;top:0;width:626px;height:720px;background:linear-gradient(160deg,#e7e6ea 0%,#cfc7c2 35%,#a98b7c 55%,#c9bfe3 80%,#b6a9d9 100%)"></div>
</section>

<section class="testimonials">
  <h2 class="title center">What our Patients are Saying</h2>
  <svg class="wave abs" style="left:411px;top:106px" width="378" height="6"><rect width="378" height="6" fill="url(#wave-dark)"/></svg>
  <svg class="abs" style="left:142px;top:262px" width="20" height="30" viewBox="0 0 20 30"><path d="M16 3 4 15l12 12" fill="none" stroke="#2f63b3" stroke-width="3.5"/></svg>
  <svg class="abs" style="left:1038px;top:262px" width="20" height="30" viewBox="0 0 20 30"><path d="M4 3l12 12L4 27" fill="none" stroke="#2f63b3" stroke-width="3.5"/></svg>
  <p class="quote">Even though the dentist is the last place I want to be, they got me right in and took care of me. I was experiencing a terrible tooth ache just before I was leaving for vacation and they made room for me and got me looked at. They determined that I needed a root canal and got me the proper medication to treat the infection while I was gone. They were able to schedule me for a root canal for the week after I returned home and got me taken care of in a day. I only had to miss a half day of work and my tooth is all fixed for now and pain free. Thanks for working me in! <a>Read More...</a></p>
  <svg class="abs" style="left:439px;top:398px" width="322" height="14" viewBox="0 0 322 14"><path d="M0 7H153l8 7 8-7H322" fill="none" stroke="#9a97ad"/></svg>
  <div class="avatar" role="img" aria-label="Patient portrait" style="left:508px;top:443px;width:66px;height:66px;background:linear-gradient(135deg,#c9c9c9,#8a8a8a)"></div>
  <div class="avatar" role="img" aria-label="Patient portrait" style="left:626px;top:443px;width:66px;height:66px;background:linear-gradient(135deg,#d6d6d6,#7d7d7d)"></div>
  <div class="avatar" role="img" aria-label="Featured patient portrait" style="left:558px;top:434px;width:84px;height:84px;border-color:#4d68b8;background:linear-gradient(135deg,#f0c7a4,#c0673c)"></div>
  <div class="dots"><span></span><span class="on"></span><span></span></div>
</section>

<section class="why">
  <h2 class="title center">Why Choose Us</h2>
  <svg class="wave abs" style="left:500px;top:122px" width="200" height="6"><rect width="200" height="6" fill="url(#wave-light)"/></svg>
  <div class="abs" style="left:448px;top:218px;width:1px;height:212px;background:#8b84b6"></div>
  <div class="abs" style="left:752px;top:218px;width:1px;height:212px;background:#8b84b6"></div>
  <div class="abs" style="left:448px;top:456px;width:1px;height:216px;background:#8b84b6"></div>
  <div class="abs" style="left:752px;top:456px;width:1px;height:216px;background:#8b84b6"></div>
  <div class="abs" style="left:160px;top:443px;width:280px;height:1px;background:#8b84b6"></div>
  <div class="abs" style="left:460px;top:443px;width:282px;height:1px;background:#8b84b6"></div>
  <div class="abs" style="left:762px;top:443px;width:282px;height:1px;background:#8b84b6"></div>

  <div class="feature" style="left:148px;top:238px">
    <svg width="60" height="60" viewBox="0 0 60 60" fill="none" stroke="#e0862c" stroke-width="2"><rect x="8" y="6" width="44" height="20" rx="3"/><path d="M14 26v10h32V26M18 36v14M42 36v14M12 50h36"/><circle cx="30" cy="42" r="5"/></svg>
    <h3>Clear Aligners</h3>
    <p>Lorem ipsum dolor sit amet, consectetur adipiscing elit, sed d o eiusmod tempor incididun.</p>
  </div>
  <div class="feature" style="left:452px;top:238px">
    <svg width="60" height="60" viewBox="0 0 60 60" fill="none" stroke="#e0862c" stroke-width="2"><path d="M16 6c-8 0-10 9-8 18 2 8 4 12 5 22 1 7 6 8 8 2l3-12c1-3 5-3 6 0l3 12c2 6 7 5 8-2 1-10 3-14 5-22 2-9 0-18-8-18-5 0-8 3-14 3S21 6 16 6Z"/></svg>
    <h3>Teeth Whitening</h3>
    <p>Lorem ipsum dolor sit amet, consectetur adipiscing elit, sed d o eiusmod tempor incididun.</p>
  </div>
  <div class="feature" style="left:754px;top:238px">
    <svg width="60" height="60" viewBox="0 0 60 60" fill="none" stroke="#e0862c" stroke-width="2"><path d="M12 30l18-9 18 9-18 9Z M12 30v16l18 9 18-9V30M30 39v16"/><path d="M36 18c-2-6 2-12 8-12s8 6 6 10-4 6-4 10"/><path d="M52 10l4-3M54 18h4"/></svg>
    <h3>Non-Surgical Root Canal</h3>
    <p>Lorem ipsum dolor sit amet, consectetur adipiscing elit, sed d o eiusmod tempor incididun.</p>
  </div>
  <div class="feature" style="left:148px;top:488px">
    <svg width="60" height="60" viewBox="0 0 60 60" fill="none" stroke="#e0862c" stroke-width="2"><path d="M10 4h26l8 8v42H10Z"/><circle cx="24" cy="22" r="8"/><path d="M24 14v8h8"/><path d="M30 54V38h6v16M40 54V30h6v16M50 54V42"/></svg>
    <h3>Sedation Dentistry</h3>
    <p>Lorem ipsum dolor sit amet, consectetur adipiscing elit, sed d o eiusmod tempor incididun.</p>
  </div>
  <div class="feature" style="left:452px;top:488px">
    <svg width="60" height="60" viewBox="0 0 60 60" fill="none" stroke="#e0862c" stroke-width="2"><rect x="8" y="14" width="34" height="26" rx="3"/><path d="M16 24h18M16 31h12M42 20h8l4-6M8 40l-2 8"/><circle cx="46" cy="40" r="6"/></svg>
    <h3>Child Dentistry</h3>
    <p>Lorem ipsum dolor sit amet, consectetur adipiscing elit, sed d o eiusmod tempor incididun.</p>
  </div>
  <div class="feature" style="left:754px;top:488px">
    <svg width="60" height="60" viewBox="0 0 60 60" fill="none" stroke="#e0862c" stroke-width="2"><circle cx="18" cy="12" r="5"/><circle cx="30" cy="10" r="5"/><circle cx="42" cy="12" r="5"/><path d="M10 28c0-6 4-9 8-9s8 3 8 9M22 26c0-6 4-9 8-9s8 3 8 9M34 28c0-6 4-9 8-9s8 3 8 9"/><path d="M6 40h14l10 6 18-8c4-1 6 3 2 5L30 54H6"/></svg>
    <h3>Advanced Technologyy</h3>
    <p>Lorem ipsum dolor sit amet, consectetur adipiscing elit, sed d o eiusmod tempor incididun.</p>
  </div>
</section>

<section class="schedule">
  <h2 class="title center">Schedule a Free Dental Implant Consultation!</h2>
  <svg class="wave abs" style="left:298px;top:110px" width="604" height="6"><rect width="604" height="6" fill="url(#wave-dark)"/></svg>
  <div class="schedule-copy">
    <p>Dental implants have helped thousands of people change their lives and Bright Molar Studio is the place to go in Fairview for the service. With dental implants, you'll be able to eat the foods you used to eat. You'll laugh again without feeling self-conscious, without feeling that something embarrassing will happen.</p>
    <p>You'll be able to interact with people just like you did when you had natural teeth. Dental implants can restore your self-confidence too. In addition to eating what foods you want, foods like apples and fresh vegetables, you'll be healthier because you'll be able to digest your food better. You see, without chewing your food completely, your body can't digest it properly. But with dental implants, you'll have almost as much biting and chewing powers as you did when you had natural teeth. Schedule a free consultation to meet with Dr. Ferrow and learn how dental implants can change your life.</p>
  </div>
  <a class="btn">Schedule a Free Consultation</a>
</section>

<section class="contact">
  <div class="map" role="img" aria-label="Street map showing the clinic location and nearby roads"></div>
  <h2 class="title">Get In touch</h2>
  <svg class="wave abs" style="left:695px;top:100px" width="156" height="6"><rect width="156" height="6" fill="url(#wave-light)"/></svg>
  <div class="field" style="top:150px;height:32px">Your Name</div>
  <div class="field" style="top:201px;height:32px">Your Email</div>
  <div class="field" style="top:251px;height:93px">Your Message</div>
  <div class="submit">Submit</div>
</section>

<footer class="site-footer">
  <div class="fcol" style="left:146px">
    <h4>Services</h4>
    <svg class="wave" style="margin-top:6px" width="86" height="6"><rect width="86" height="6" fill="url(#wave-dark)"/></svg>
    <ul><li>Home</li><li>Portfolio</li><li>Free Resources</li><li>About Us</li><li>Terms &amp; Conditions</li><li>Sitemap</li></ul>
  </div>
  <div class="fcol" style="left:337px">
    <h4>Company</h4>
    <svg class="wave" style="margin-top:6px" width="86" height="6"><rect width="86" height="6" fill="url(#wave-dark)"/></svg>
    <ul><li>Home</li><li>Portfolio</li><li>Free Resources</li><li>About Us</li><li>Terms &amp; Conditions</li><li>Sitemap</li></ul>
  </div>
  <div class="fcol" style="left:530px">
    <h4>Latest Articles</h4>
    <svg class="wave" style="margin-top:6px" width="86" height="6"><rect width="86" height="6" fill="url(#wave-dark)"/></svg>
    <div style="margin-top:30px">
      <div class="article"><div class="thumb" role="img" aria-label="Article thumbnail"></div><p>Lorem ipsum dolor sit amet, conse cterud , cons ectetur, adipis ci velit, sed .<time>1 Dec, 2020</time></p></div>
      <div class="article"><div class="thumb" role="img" aria-label="Article thumbnail"></div><p>Lorem ipsum dolor sit amet, conse cterud , cons ectetur, adipis ci velit, sed .<time>1 Dec, 2020</time></p></div>
      <div class="article"><div class="thumb" role="img" aria-label="Article thumbnail"></div><p>Lorem ipsum dolor sit amet, conse cterud , cons ectetur, adipis ci velit, sed .<time>1 Dec, 2020</time></p></div>
    </div>
  </div>
  <div class="fcol" style="left:904px">
    <h4>Let's Connect</h4>
    <svg class="wave" style="margin-top:6px" width="86" height="6"><rect width="86" height="6" fill="url(#wave-dark)"/></svg>
    <div style="margin-top:34px">
      <div class="connect"><svg width="18" height="16" viewBox="0 0 18 16"><path d="M4 1C2 2 1.5 4 3 7c1.6 3 4 5.3 7 6.6 2 .8 3.6.3 4.4-1.2L12 10l-1.8 1.1C8.5 10.3 7 8.8 6.2 7l1.1-1.8Z" fill="none" stroke="#4d68b8" stroke-width="1.4"/></svg>555 014 2287</div>
      <div class="connect"><svg width="18" height="18" viewBox="0 0 18 18"><path d="M9 1a5.5 5.5 0 0 0-5.5 5.5C3.5 11 9 17 9 17s5.5-6 5.5-10.5A5.5 5.5 0 0 0 9 1Z" fill="#4d68b8"/><circle cx="9" cy="6.5" r="2" fill="#fff"/></svg><span>418 alder ln 120<br>fairview OH 43999</span></div>
      <div class="connect"><svg width="18" height="16" viewBox="0 0 18 16"><path d="M1 8 17 1 13 15 9 10Z M9 10 17 1" fill="none" stroke="#4d68b8" stroke-width="1.4"/></svg>care@brightmolarstudio.com</div>
    </div>
  </div>
  <div class="rule"></div>
</footer>
</body>
</html>
```